HAIR EXTENSIONS

We need a web design for a company base in Chicago called Extensions by Corvella. We sale 100% human hair in Brazilian body wave deep wave straight or natural curl, Peruvian body wave straight or deep wave. Malaysian loose straight or body wave, in the chicago land.
We also ship hair to any city or country. We like to see design that use the colors pinks & grays, or would just like to see some design creative with colors thats inviting.

Also I'm using the quillmoss template, Home- banner contact us, about us, Features- product side/left sidebar, Shop- wish list /shopping cart/ tracking your order / checkout/ order received.
Porfolio-filterable 4column portfolio
Blog. Buy now

Industry/Entity Type

Hair

Number of Pages Required

4 page

Colors
aaaaaa
606060
dddddd
eea4c8
d3a5cc
b868aa
a6459a
ffc213
1b1b1b

Requirements
Must have
• I NEED THE DESIGNER TO DO THE 4 PAGE LIKE THIS.
• 1.HOME-PAGE BANNER CONTACT US SOME PRODUCT WITH SIDING IMAGES OF THE TOP PROUDCT
• 2.PRODUCT WITH SHOPPING CART- I WANT SIDING BARS FOR PRODUCT & SHOPPING CART WITH TRACKING YOUR ORDERS CHECK OUT & ORDER RECEIVED.
• 3.PORFOLIO PHOTO-I WANT A FEATURES FOR CUSTOMERS TO UPLOAN THERE PICTURE & BLOG ON THE PAGE
• 4.ABOUT US- TALK ABOUT ARE COMPAMY.
Nice to have
• hello designer
• I was working with a web developer for my site be for i came to pixelharborr & they build a site for me that i liked, You all can view it at www.Extensionsbycorvella.info
• long story short never could get them to finish the project after they got paid!!
• I know, why paid before its finish bad decision. So know I'm here starting over with you all.
• here is a list of my competition site
• www.lockshaventress.com
• www.velmatrade.com
• www.orlitasparlor.com
• So just to give some insight, I'm looking for something like the one i had builded.

```html
<!DOCTYPE html>
<html lang="en">
<head>
<meta charset="utf-8">
<title>Extensions by Corvella</title>
<link href="https://fonts.googleapis.com/css2?family=Raleway:wght@300;400;500&family=Gentium+Book+Plus:wght@400;700&display=swap" rel="stylesheet">
<style>
  :root {
    --pink: #f2136f;
    --pink-deep: #e60c66;
    --pink-soft: #f93d8a;
    --plum: #5a0a2c;
    --ink: #0b0b0b;
    --white: #ffffff;
    --grey-line: #dddddd;
    --grey-mid: #aaaaaa;
    --hair-dark: #6e4a2a;
    --hair-light: #b48a5a;
  }
  * { box-sizing: border-box; margin: 0; padding: 0; }
  html, body { width: 1200px; height: 720px; overflow: hidden; background: var(--white); }
  body { position: relative; font-family: 'Raleway', sans-serif; }

  .sidebar { position: absolute; left: 0; top: 0; width: 277px; height: 720px; background: var(--pink); }
  .brand { position: absolute; left: 32px; top: 62px; display: flex; align-items: center; gap: 8px; }
  .brand-dot { width: 14px; height: 14px; border-radius: 50%; background: var(--plum); }
  .brand-name { font-family: 'Raleway', sans-serif; font-weight: 400; font-size: 24px; line-height: 1.1; color: var(--plum); width: 190px; }

  .main-nav { position: absolute; right: 26px; top: 224px; text-align: right; list-style: none; }
  .main-nav li { font-weight: 300; font-size: 30px; color: var(--white); height: 61px; line-height: 48px; }
  .main-nav .caret { display: inline-block; margin-left: 12px; width: 0; height: 0; border-left: 6px solid transparent; border-right: 6px solid transparent; border-top: 6px solid var(--white); vertical-align: middle; }
  .nav-marker { position: absolute; left: 278px; top: 225px; width: 4px; height: 41px; background: var(--grey-mid); }

  .search { position: absolute; left: 24px; top: 415px; width: 225px; height: 48px; background: var(--pink-deep); color: rgba(255,255,255,0.85); font-weight: 300; font-size: 19px; line-height: 48px; padding-left: 20px; }
  .copyright { position: absolute; left: 24px; top: 675px; font-size: 13px; color: var(--white); }

  .topbar { position: absolute; left: 277px; top: 0; width: 923px; height: 39px; background: linear-gradient(90deg, #d4d4d4, #f2f2f2 50%, #cfcfcf); }
  .topbar-link { position: absolute; top: 6px; display: flex; align-items: center; gap: 9px; font-size: 12px; color: var(--ink); }
  .topbar-link .icon { width: 28px; height: 28px; border-radius: 50%; background: var(--white); display: flex; align-items: center; justify-content: center; }

  .hero { position: absolute; left: 277px; top: 39px; width: 923px; height: 441px; background: radial-gradient(ellipse at 35% 55%, #f4f4f4 0%, #c9c9c9 60%, #9d9d9d 100%); }
  .hero-model { position: absolute; left: 520px; top: 50px; width: 400px; height: 391px; background: linear-gradient(180deg, #c9a06a 0%, #a57a4a 55%, #1f1f1f 100%); opacity: 0.85; }
  .hero-copy { position: absolute; left: 84px; top: 150px; }
  .hero-title { font-weight: 300; font-size: 48px; color: var(--ink); line-height: 1; }
  .hero-sub { font-weight: 500; font-size: 24px; color: var(--ink); margin-top: 4px; }
  .hero-price { font-weight: 300; font-size: 31px; color: var(--pink); margin-top: 6px; }
  .btn-dark { position: absolute; left: 86px; top: 313px; width: 110px; height: 32px; background: var(--ink); color: var(--white); font-family: 'Gentium Book Plus', serif; font-weight: 700; font-size: 15px; display: flex; align-items: center; justify-content: center; gap: 10px; border-bottom: 2px solid var(--white); box-shadow: 0 2px 0 var(--ink); }
  .tri { width: 0; height: 0; border-top: 5px solid transparent; border-bottom: 5px solid transparent; border-left: 5px solid currentColor; }

  .products { position: absolute; left: 277px; top: 480px; width: 923px; height: 240px; }
  .product { position: absolute; top: 0; width: 308px; height: 240px; }
  .product + .product { border-left: 2px solid var(--grey-line); }
  .product-photo { position: absolute; left: 84px; top: 15px; width: 118px; height: 213px; border-radius: 40% 40% 50% 10%; background: linear-gradient(180deg, var(--hair-dark), var(--hair-light)); }
  .product-card { position: absolute; left: 9px; top: 9px; width: 289px; height: 222px; background: var(--pink-soft); }
  .product-card .frame { position: absolute; inset: 10px; border: 1px solid rgba(255,255,255,0.9); text-align: center; color: var(--white); font-family: 'Gentium Book Plus', serif; }
  .product-card h3 { font-weight: 400; font-size: 28px; margin-top: 30px; }
  .product-card .price { font-size: 26px; margin-top: 10px; }
  .btn-light { margin: 11px auto 0; width: 111px; height: 32px; background: var(--white); color: #444; font-size: 15px; display: flex; align-items: center; justify-content: center; gap: 10px; box-shadow: 0 2px 0 var(--white), 0 3px 0 #aaa; }
</style>
</head>
<body>
  <aside class="sidebar">
    <div class="brand"><span class="brand-name">Extensions by Corvella</span><span class="brand-dot"></span></div>
    <ul class="main-nav">
      <li>Home</li>
      <li>Products<span class="caret"></span></li>
      <li>Contact</li>
    </ul>
    <div class="search">Search...</div>
    <p class="copyright">Copyright © 2014 Extensions by Corvella</p>
  </aside>
  <div class="nav-marker"></div>

  <header class="topbar">
    <div class="topbar-link" style="left:706px">
      <span class="icon"><svg width="13" height="12" viewBox="0 0 24 22"><path d="M12 21 2 11a6 6 0 0 1 10-7 6 6 0 0 1 10 7z" fill="#0b0b0b"/></svg></span>My Wishlist
    </div>
    <div class="topbar-link" style="left:829px">
      <span class="icon"><svg width="13" height="12" viewBox="0 0 24 22"><path d="M1 2h4l3 12h12l3-9H7" fill="none" stroke="#0b0b0b" stroke-width="3"/><path d="M7 5h16l-3 9H8z" fill="#0b0b0b"/><circle cx="10" cy="19" r="2" fill="#0b0b0b"/><circle cx="19" cy="19" r="2" fill="#0b0b0b"/></svg></span>My Cart
    </div>
  </header>

  <section class="hero">
    <div class="hero-model" role="img" aria-label="Photo of a model with long blonde wavy hair extensions"></div>
    <div class="hero-copy">
      <h1 class="hero-title">Lumi Hair</h1>
      <p class="hero-sub">awesome extension</p>
      <p class="hero-price">in just $97</p>
    </div>
    <div class="btn-dark"><span class="tri"></span>View all</div>
  </section>

  <section class="products">
    <div class="product" style="left:0">
      <div class="product-photo" role="img" aria-label="Brown highlighted hair topper piece"></div>
    </div>
    <div class="product" style="left:308px">
      <div class="product-card">
        <div class="frame">
          <h3>Thinning hair</h3>
          <p class="price">$99</p>
          <div class="btn-light"><span class="tri"></span>Buy now</div>
        </div>
      </div>
    </div>
    <div class="product" style="left:616px">
      <div class="product-photo" role="img" aria-label="Brown highlighted hair topper piece"></div>
    </div>
  </section>
</body>
</html>
```